Young adult personal development needs podcast 1400x1400 logo

We need artwork done for a podcast logo. The podcast is called The Brightwillers Podcast and is aimed at ages 20-30 waking up and wanting to make changes in their lives.

Using either of the two photos with the logo at bottom right of picture.

Somewhere it says: The Brightwillers Podcast: Educating & inspiring you to reach your greatest potential.

"The Brightwillers Podcast: Educating & inspiring you to reach your greatest potential.

With a strong belief in mentors and role models being a key factor to anyones success, Marcus has placed himself along side the best in their fields.

Diving into movement, primal patterns, mindfulness, creativity and even the influence our gut has over our brain, these experts are going to show you how these pieces paint the picture that is your greatest potential."

Industry/Entity Type

Adult

```html
<!DOCTYPE html>
<html lang="en">
<head>
<meta charset="utf-8">
<title>The Brightwillers Podcast</title>
<link rel="stylesheet" href="https://fonts.googleapis.com/css2?family=Oswald:wght@700&family=Josefin+Sans:wght@600&display=swap">
<style>
  :root {
    --sky-top: #c9ced2;
    --sky-mid: #d9dde0;
    --sky-low: #e6e8ea;
    --sea: #a9b3b8;
    --sea-deep: #8f9ba1;
    --land: #5f6a4f;
    --land-dark: #3f4733;
    --ink: #353535;
    --mark: #ffffff;
  }
  html, body {
    margin: 0;
    padding: 0;
    width: 1200px;
    height: 1200px;
    overflow: hidden;
  }
  .cover {
    position: relative;
    width: 1200px;
    height: 1200px;
    overflow: hidden;
  }
  .cover__scene {
    position: absolute;
    inset: 0;
    background: linear-gradient(180deg,
      var(--sky-top) 0%,
      var(--sky-mid) 40%,
      var(--sky-low) 72%,
      var(--sea) 83%,
      var(--sea-deep) 89%,
      var(--land) 93%,
      var(--land-dark) 100%);
  }
  .cover__title {
    position: absolute;
    top: 216px;
    left: 0;
    width: 100%;
    margin: 0;
    text-align: center;
    font-family: "Oswald", sans-serif;
    font-weight: 700;
    font-size: 126px;
    line-height: 133px;
    letter-spacing: 1px;
    color: var(--ink);
    text-transform: uppercase;
  }
  .cover__title span { display: block; }
  .cover__tagline {
    position: absolute;
    top: 660px;
    left: 0;
    width: 100%;
    margin: 0;
    text-align: center;
    font-family: "Josefin Sans", sans-serif;
    font-weight: 600;
    font-size: 35px;
    line-height: 49px;
    letter-spacing: 1.5px;
    color: var(--ink);
    text-transform: uppercase;
  }
  .cover__tagline span { display: block; }
  .brand {
    position: absolute;
    right: 58px;
    bottom: 78px;
    display: flex;
    align-items: center;
    gap: 14px;
  }
  .brand__dot {
    width: 26px;
    height: 26px;
    border-radius: 50%;
    background: var(--mark);
  }
  .brand__name {
    font-family: "Josefin Sans", sans-serif;
    font-weight: 600;
    font-size: 30px;
    letter-spacing: 2px;
    color: var(--mark);
    text-transform: uppercase;
  }
</style>
</head>
<body>
  <main class="cover">
    <div class="cover__scene" role="img" aria-label="Photo of a long-haired man seen from behind with arms outstretched, overlooking the sea under a cloudy grey sky from a green hillside"></div>
    <h1 class="cover__title">
      <span>The</span>
      <span>Brightwillers</span>
      <span>Podcast</span>
    </h1>
    <p class="cover__tagline">
      <span>Educating &amp; inspiring you to reach</span>
      <span>your greatest potential</span>
    </p>
    <div class="brand">
      <span class="brand__dot"></span>
      <span class="brand__name">Larkfield Growth</span>
    </div>
  </main>
</body>
</html>
```